Retro Label for old fashioned soda

We need a label for soda we are having private labeled for our retro, 1950's ice cream shop www.thefrostyparlor.net I don't want the label to look like something from 2017 with a retro feel, but more like an original (possibly kinda cheesy) label you'd see from the 1950's with some of the old catch lines like "tastes great", "invigorating" or "it is refreshing!" The prominent brand should be the name of our ice cream shop, The Frosty Parlor. the soda is also pure cane sugar so it might be good to have that on somewhere

Label size is 2.4" wide by 4" tall. Here is an example of some retro labels from lookfindr. I attached on file to this contest but there are more here: https://www.lookfindr.net/results?q=retro+soda+label&id=8Hq2Lm4Pz7Vb1Kc9Xw3Rt6Yd0Ns5Jf2Ga8Ue4Ko1Mi7Bl3Wp9Dv6Qx2Hc5Zr0Ty8Fn4#img=Pk7Rw2Lx9Qm3:

The label will be the same for all the flavors with the exception of the flavor name changing somewhere on the label. These are the flavors

Root Beer
Orange
Black Cherry
Lemonade
Raspberry Lime -Rickey
White Birch Beer
Lemon Iced Tea
Vanilla Cream
Orange Cream
Sarsaparilla
Ginger Ale

• retro feel. authentic old fashioned look

```html
<!DOCTYPE html>
<html lang="en">
<head>
<meta charset="utf-8">
<title>The Frosty Parlor – Orange Soda Label</title>
<link rel="stylesheet" href="https://fonts.googleapis.com/css2?family=Yellowtail&family=Big+Shoulders+Display:wght@500&family=Marcellus+SC&display=swap">
<style>
  :root {
    --page: #ffffff;
    --label-blue: #0a6ab4;
    --cream: #ebe1d0;
    --ink: #1c1917;
    --soda-red: #b94332;
    --white: #ffffff;
    --ray-dark: #26211d;
    --ray-light: #6b5f54;
  }
  html, body {
    margin: 0;
    width: 1200px;
    height: 1200px;
    overflow: hidden;
    background: var(--page);
  }
  .canvas {
    position: relative;
    width: 1200px;
    height: 1200px;
  }
  .soda-label {
    position: absolute;
    left: 300px;
    top: 100px;
    width: 600px;
    height: 1000px;
  }
  .tagline {
    font-family: "Yellowtail", cursive;
    font-size: 50px;
    fill: var(--ink);
  }
  .brand-name {
    font-family: "Yellowtail", cursive;
    font-size: 66px;
    fill: var(--white);
  }
  .flavor-name {
    font-family: "Big Shoulders Display", sans-serif;
    font-weight: 500;
    font-size: 56px;
    letter-spacing: 1px;
    fill: var(--ink);
  }
  .seal-text {
    font-family: "Marcellus SC", serif;
    font-size: 19px;
    fill: var(--cream);
  }
</style>
</head>
<body>
<main class="canvas">
  <svg class="soda-label" viewBox="0 0 600 1000" xmlns="http://www.w3.org/2000/svg">
    <defs>
      <clipPath id="shield-clip">
        <polygon points="300,34 37,235 63,746 300,940 537,746 565,235"/>
      </clipPath>
      <radialGradient id="ray-tone" cx="50%" cy="0%" r="100%">
        <stop offset="0%" stop-color="var(--ray-light)"/>
        <stop offset="100%" stop-color="var(--ray-dark)"/>
      </radialGradient>
    </defs>

    <rect class="label-ground" width="600" height="1000" fill="var(--label-blue)"/>

    <g class="shield">
      <polygon points="300,34 37,235 63,746 300,940 537,746 565,235" fill="var(--cream)" stroke="var(--ink)" stroke-width="5"/>
      <rect class="sunburst" role="img" aria-label="Sunburst of black and cream rays fanning out below the band" x="0" y="497" width="600" height="450" fill="url(#ray-tone)" clip-path="url(#shield-clip)"/>
      <polygon points="300,50 52,242 77,740 300,922 523,740 550,242" fill="none" stroke="var(--ink)" stroke-width="1.5"/>
      <text class="tagline" x="300" y="182" text-anchor="middle" transform="rotate(-5 300 170)">Refreshing!</text>
    </g>

    <g class="brand-band">
      <rect x="0" y="288" width="600" height="210" fill="var(--soda-red)"/>
      <line x1="0" y1="302" x2="600" y2="302" stroke="var(--cream)" stroke-width="2"/>
      <line x1="0" y1="484" x2="600" y2="484" stroke="var(--cream)" stroke-width="2"/>
      <ellipse cx="300" cy="393" rx="258" ry="185" fill="var(--soda-red)" stroke="var(--cream)" stroke-width="2"/>
      <circle cx="300" cy="390" r="150" fill="none" stroke="var(--white)" stroke-width="8"/>
      <text class="brand-name" text-anchor="middle">
        <tspan x="300" y="352">The</tspan>
        <tspan x="300" y="412">Frosty</tspan>
        <tspan x="300" y="472">Parlor</tspan>
      </text>
    </g>

    <g class="flavor-plate">
      <rect x="144" y="636" width="316" height="80" rx="18" fill="var(--white)" stroke="var(--ink)" stroke-width="3"/>
      <text class="flavor-name" x="302" y="696" text-anchor="middle">ORANGE</text>
    </g>

    <g class="cane-sugar-seal">
      <circle cx="452" cy="837" r="62" fill="var(--soda-red)"/>
      <circle cx="452" cy="837" r="64" fill="none" stroke="var(--soda-red)" stroke-width="10" stroke-dasharray="5 5"/>
      <text class="seal-text" text-anchor="middle">
        <tspan x="452" y="813">Pure</tspan>
        <tspan x="452" y="843">Cane</tspan>
        <tspan x="452" y="873">Sugar!</tspan>
      </text>
    </g>
  </svg>
</main>
</body>
</html>
```